Business Card Design

We are a manufacturing company that has been in business for over 30 years, established in 1981. We are looking to increase our business with defence force, government, and the major telecoms so the card needs to present the company as being cutting edge, secure, and professional.
Industry/Entity Type
Defence
Contact Information for Business Card
Name Gareth Olsund
Phone 02 9374 6815
Fax 02 9457 3162
mobile 0438260517
Email Gary@Korvex.com.au
Webiste www.korvex.com.au
ABN 58 006 391 842
address: 17 Belcor Street Kellmore NSW 2574
"Manufacturer of Antennas, GPS, Microwave, Cable Assemblies, RF, Military, & Telecommunications"
Look and feel

```html
<!DOCTYPE html>
<html lang="en">
<head>
<meta charset="utf-8">
<title>Korvex Business Card</title>
<link href="https://fonts.googleapis.com/css2?family=Ubuntu:wght@400;500;700&display=swap" rel="stylesheet">
<style>
  :root {
    --navy: #1b2260;
    --orange: #c8432a;
    --ink: #2b2b2b;
    --paper: #fbfbfa;
    --backdrop: #e6e6e6;
  }
  * { margin: 0; padding: 0; box-sizing: border-box; }
  html, body { width: 1200px; height: 644px; overflow: hidden; }
  body {
    background: var(--backdrop);
    font-family: "Ubuntu", Arial, sans-serif;
    color: var(--ink);
    position: relative;
  }
  .card {
    position: absolute;
    top: 160px;
    width: 499px;
    height: 301px;
    background: var(--paper);
  }
  .card--front { left: 64px; }
  .card--back { left: 639px; }

  .brand { position: absolute; }
  .brand__square { background: var(--navy); }
  .brand__name {
    display: block;
    color: var(--orange);
    font-weight: 500;
    letter-spacing: 3px;
    text-align: center;
  }
  .card--front .brand { left: 39px; top: 50px; width: 156px; }
  .card--front .brand__square { width: 156px; height: 133px; }
  .card--front .brand__name { font-size: 24px; margin-top: 18px; }
  .card--back .brand { left: 51px; top: 71px; width: 131px; }
  .card--back .brand__square { width: 131px; height: 111px; }
  .card--back .brand__name { font-size: 20px; margin-top: 15px; }

  .stripes { position: absolute; left: 0; bottom: 0; width: 100%; height: 20px; }
  .stripes__orange { position: absolute; left: 0; top: 0; width: 233px; height: 100%; background: linear-gradient(90deg, #b8351f, var(--orange)); }
  .stripes__navy { position: absolute; left: 240px; right: 0; top: 0; height: 100%; background: linear-gradient(90deg, var(--navy), #131a4d); }

  .services { position: absolute; left: 275px; top: 101px; }
  .services__title { color: var(--navy); font-size: 16px; font-weight: 700; margin-bottom: 9px; }
  .services__item { font-size: 12.5px; line-height: 25px; }
  .abn { position: absolute; left: 275px; top: 234px; color: var(--orange); font-size: 12.5px; font-weight: 500; }

  .contact { position: absolute; left: 272px; top: 61px; font-size: 12.5px; line-height: 16px; }
  .contact__name { color: var(--navy); font-size: 16px; font-weight: 700; line-height: 18px; }
  .contact__role { margin-bottom: 14px; }
  .contact__web { margin-bottom: 22px; }
  .contact__address { margin-bottom: 6px; }
  .contact__line { display: flex; align-items: center; gap: 5px; }
  .contact__line svg { width: 11px; height: 11px; flex: none; }
</style>
</head>
<body>
  <section class="card card--front">
    <div class="brand">
      <div class="brand__square"></div>
      <span class="brand__name">KORVEX</span>
    </div>
    <div class="services">
      <h2 class="services__title">Manufacturer of</h2>
      <p class="services__item">Antennas, GPS, Microwave</p>
      <p class="services__item">Cable Assemblies, RF</p>
      <p class="services__item">Military, &amp; Telecommunications</p>
    </div>
    <p class="abn">ABN 58 006 391 842</p>
    <div class="stripes"><span class="stripes__orange"></span><span class="stripes__navy"></span></div>
  </section>

  <section class="card card--back">
    <div class="brand">
      <div class="brand__square"></div>
      <span class="brand__name">KORVEX</span>
    </div>
    <div class="contact">
      <h1 class="contact__name">GARETH OLSUND</h1>
      <p class="contact__role">Director</p>
      <p class="contact__web">www.korvex.com.au</p>
      <p class="contact__address">17 Belcor Street<br>Kellmore NSW 2574</p>
      <p class="contact__line">
        <svg viewBox="0 0 12 12" aria-hidden="true"><rect x="3" y="0.5" width="6" height="11" rx="1" fill="none" stroke="#c8432a"/><line x1="5" y1="9.5" x2="7" y2="9.5" stroke="#c8432a"/></svg>
        0438260517</p>
      <p class="contact__line">
        <svg viewBox="0 0 12 12" aria-hidden="true"><circle cx="6" cy="6" r="5.3" fill="none" stroke="#c8432a"/><path d="M4 3.5 Q3 6 6 8.5 L7.5 7.5" fill="none" stroke="#c8432a"/></svg>
        02 9374 6815</p>
      <p class="contact__line">
        <svg viewBox="0 0 12 12" aria-hidden="true"><rect x="1" y="5" width="10" height="6" fill="none" stroke="#c8432a"/><rect x="3" y="1" width="6" height="4" fill="none" stroke="#c8432a"/></svg>
        02 9457 3162</p>
      <p class="contact__line">
        <svg viewBox="0 0 12 12" aria-hidden="true"><rect x="0.5" y="2.5" width="11" height="7" fill="none" stroke="#c8432a"/><path d="M0.5 2.5 L6 6.5 L11.5 2.5" fill="none" stroke="#c8432a"/></svg>
        Gary@Korvex.com.au</p>
    </div>
    <div class="stripes"><span class="stripes__orange"></span><span class="stripes__navy"></span></div>
  </section>
</body>
</html>
```